Harbor Nightclub

Nightclub flyer., digital single sided, for KV and PX. I included samples of some previous flyers we've used. Sample Info:
HARBOR
FRIDAYS
FRI MAY 1 2020
DJ VORTAN (club floor)
DJ RUZO & DJ TAV (residents on the lounge floor)
4217 Marlow Avenue Sacramento
www.harborvenuehall.example for list/VIP inquiries

Target Market(s)

Upscale top 40 crowd but want some cool and artsy like the examples included.

Font styles to use
Sans Serif

Requirements
Must have
• Harbor Logo
Nice to have
• Would be nice if the flyer can be incorporated later with DJ photos (sometimes we will add dj photos to pixagram etc). Would like a big city type of feel.
Should not have
• Nothing too sexual.

```html
<!DOCTYPE html>
<html lang="en">
<head>
<meta charset="utf-8">
<title>Harbor Friday Night</title>
<link rel="stylesheet" href="https://fonts.googleapis.com/css2?family=Montserrat:wght@400;500;600;700;800&family=Allura&display=swap">
<style>
  :root {
    --night-deep: #0f0a2a;
    --night-purple: #2c1758;
    --night-violet: #4a2a86;
    --glow-magenta: #c2205e;
    --glow-red: #8f1e4a;
    --white: #ffffff;
    --silver: #d9dbe6;
    --script-yellow: #f6ec4a;
    --cream: #f6efbf;
  }
  * { margin: 0; padding: 0; box-sizing: border-box; }
  html, body { width: 1200px; height: 1200px; overflow: hidden; background: var(--night-deep); }
  .flyer {
    position: relative;
    width: 1200px;
    height: 1200px;
    overflow: hidden;
    font-family: "Montserrat", sans-serif;
    color: var(--white);
  }
  .club-photo {
    position: absolute;
    inset: 0;
    background:
      radial-gradient(ellipse 520px 300px at 900px 170px, rgba(194,32,94,0.75), transparent 70%),
      radial-gradient(ellipse 480px 260px at 250px 200px, rgba(143,30,74,0.6), transparent 70%),
      radial-gradient(ellipse 500px 220px at 560px 330px, rgba(200,60,60,0.35), transparent 70%),
      radial-gradient(ellipse 700px 400px at 600px 620px, rgba(74,42,134,0.8), transparent 75%),
      linear-gradient(180deg, #3a1c5e 0%, var(--night-purple) 45%, #241347 70%, var(--night-deep) 100%);
  }
  .bottom-shade {
    position: absolute;
    left: 0; right: 0; bottom: 0;
    height: 560px;
    background: linear-gradient(180deg, transparent 0%, rgba(15,10,42,0.65) 45%, rgba(12,8,34,0.92) 100%);
  }
  .brand {
    position: absolute;
    top: 58px;
    left: 0; right: 0;
    text-align: center;
  }
  .brand-mark {
    display: block;
    width: 80px; height: 80px;
    margin: 0 auto;
    border-radius: 50%;
    background: var(--silver);
  }
  .brand-name {
    display: block;
    margin-top: 22px;
    font-size: 40px;
    font-weight: 500;
    letter-spacing: 2px;
    color: var(--white);
  }
  .headline {
    position: absolute;
    top: 648px;
    left: 0; right: 0;
    text-align: center;
    font-size: 156px;
    font-weight: 700;
    letter-spacing: -2px;
    line-height: 1;
    color: var(--white);
    text-shadow: 0 4px 10px rgba(0,0,0,0.45);
  }
  .subtitle {
    position: absolute;
    top: 735px;
    left: 0; right: 0;
    text-align: center;
    font-family: "Allura", cursive;
    font-size: 168px;
    line-height: 1;
    color: var(--script-yellow);
    transform: rotate(-4deg);
  }
  .lineup {
    position: absolute;
    top: 950px;
    left: 0; right: 0;
    text-align: center;
    font-size: 37px;
    font-weight: 700;
    color: var(--cream);
  }
  .date {
    position: absolute;
    top: 1008px;
    left: 0; right: 0;
    text-align: center;
    font-size: 21px;
    font-weight: 500;
    letter-spacing: 1px;
    color: var(--cream);
  }
  .inquiries {
    position: absolute;
    top: 1050px;
    left: 0; right: 0;
    text-align: center;
    font-size: 21px;
    font-weight: 700;
    letter-spacing: 0.5px;
    color: var(--cream);
  }
  .address {
    position: absolute;
    top: 1091px;
    left: 0; right: 0;
    text-align: center;
    font-size: 21px;
    font-weight: 500;
    letter-spacing: 4px;
    color: var(--white);
  }
  .address sup { font-size: 12px; letter-spacing: 2px; }
</style>
</head>
<body>
  <main class="flyer">
    <div class="club-photo" role="img" aria-label="Photo of a DJ mixing console in the foreground with a crowd and colourful club lights behind"></div>
    <div class="bottom-shade"></div>

    <header class="brand">
      <span class="brand-mark"></span>
      <span class="brand-name">HARBOR</span>
    </header>

    <h1 class="headline">HARBOR</h1>
    <p class="subtitle">Friday Night</p>

    <p class="lineup">DJ VORTAN // DJ RUZO &amp; DJ TAV</p>
    <p class="date">FRIDAY . MAY 1 . 2020</p>
    <p class="inquiries">FOR LIST/VIP INQUIRIES : WWW.HARBORVENUEHALL.EXAMPLE</p>
    <p class="address">4217 MARLOW AVENUE, SACRAMENTO</p>
  </main>
</body>
</html>
```